Visitenkarten-Design für Kfz-Werkstatt von Frauen für Frauen
Zielgruppe
Kfz-Werkstatt von Frauen für Frauen
Aufgabenstellung
Die Farben des Logos sollen sich in der Visitenkarte wieder spiegeln. Darf sehr feminin gehalten werden!
Infos auf der Visistenkarte:

```html
<!DOCTYPE html>
<html lang="de">
<head>
<meta charset="utf-8">
<title>Visitenkarte Vellbach GmbH</title>
<link rel="stylesheet" href="https://fonts.googleapis.com/css2?family=Jost:wght@400;500&display=swap">
<style>
  :root {
    --stage: #302c64;
    --paper: #f3f2f2;
    --text-grey: #7d7d7d;
    --rose-light: #ecc3d0;
    --rose-mid: #e8aec0;
    --rose-deep: #a24d6c;
    --brand-pink: #e2336f;
    --rule-grey: #8a8a8a;
  }
  * { box-sizing: border-box; margin: 0; padding: 0; }
  html, body {
    width: 1200px;
    height: 785px;
    overflow: hidden;
    background: var(--stage);
    font-family: "Jost", sans-serif;
  }
  .sheet {
    position: relative;
    width: 1200px;
    height: 785px;
  }
  .card {
    position: absolute;
    top: 218px;
    width: 540px;
    height: 349px;
    background: var(--paper);
    overflow: hidden;
    box-shadow: 0 18px 40px rgba(10, 8, 40, 0.45);
  }
  .card--front { left: 45px; }
  .card--back { left: 615px; }

  /* Front */
  .front-shapes {
    position: absolute;
    inset: 0;
    width: 100%;
    height: 100%;
  }
  .front-brand {
    position: absolute;
    top: 22px;
    right: 28px;
    display: flex;
    align-items: center;
    gap: 8px;
    font-weight: 500;
    font-size: 17px;
    letter-spacing: 1.5px;
    color: var(--brand-pink);
  }
  .brand-dot {
    width: 12px;
    height: 12px;
    border-radius: 50%;
    background: var(--brand-pink);
  }
  .front-address {
    position: absolute;
    left: 40px;
    top: 150px;
    color: var(--text-grey);
    font-size: 33px;
    line-height: 1.05;
    font-weight: 400;
  }
  .front-phone {
    position: absolute;
    left: 40px;
    top: 262px;
    color: var(--text-grey);
    font-size: 30px;
    letter-spacing: 2px;
  }
  .front-footer {
    position: absolute;
    left: 0;
    right: 0;
    bottom: 0;
    height: 38px;
    background: var(--rose-light);
    display: flex;
    align-items: center;
    justify-content: center;
    gap: 16px;
    color: var(--rose-deep);
    font-size: 17px;
    letter-spacing: 0.5px;
  }

  /* Back */
  .back-wash {
    position: absolute;
    left: 40px;
    top: 50px;
    width: 470px;
    height: 260px;
    border-radius: 48% 52% 44% 56% / 55% 40% 60% 45%;
    background: radial-gradient(ellipse at 50% 50%, #e9b9c8 0%, #efcad6 45%, rgba(243, 242, 242, 0) 75%);
  }
  .back-rule {
    position: absolute;
    left: 0;
    right: 0;
    top: 182px;
    height: 3px;
    background: var(--rule-grey);
  }
  .back-brand {
    position: absolute;
    left: 0;
    right: 0;
    top: 126px;
    display: flex;
    align-items: center;
    justify-content: center;
    gap: 14px;
    font-weight: 500;
    font-size: 44px;
    letter-spacing: 4px;
    color: var(--brand-pink);
  }
  .back-brand .brand-dot {
    width: 26px;
    height: 26px;
  }
</style>
</head>
<body>
<main class="sheet">

  <section class="card card--front" aria-label="Visitenkarte Vorderseite">
    <svg class="front-shapes" viewBox="0 0 540 349" aria-hidden="true">
      <polygon points="0,0 540,0 540,92 165,140 150,118" fill="var(--rose-light)"/>
      <polygon points="150,118 540,75 540,92 165,140" fill="var(--rose-deep)"/>
    </svg>
    <div class="front-brand"><span class="brand-dot"></span>VELLBACH</div>
    <p class="front-address">Vellbach GmbH<br>Lindenauer Str. 12<br>80999 Talhausen</p>
    <p class="front-phone">0160 - 55 24 87 3</p>
    <footer class="front-footer">
      <span>hallo@kfz-rosawerk.de</span>
      <span>|</span>
      <span>www.kfz-rosawerk.de</span>
    </footer>
  </section>

  <section class="card card--back" aria-label="Visitenkarte Rückseite">
    <div class="back-wash" role="img" aria-label="Rosa Aquarellfläche als Hintergrund"></div>
    <div class="back-rule"></div>
    <div class="back-brand"><span class="brand-dot"></span>VELLBACH</div>
  </section>

</main>
</body>
</html>
```